Business card design incorporating discount offer

We are a trade services company and we need a double sided business card that is going to be used by our tradesmen to give to customers on completion of their jobs.

Below are the key elements of the card that we would like to include:

-Main logo with text 'Expert Property Care' underneath.
-Up to 12 smaller icon logos with text 'Your local all-trade experts' to emphasise the point that we cover all the trades
-Discount offer - 10% discount
-Telephone number and website address
-Blank space for tradesman to enter his/her name
-Request for customer feedback with feedback url

This business card will be printed on regular card. In the past we have favoured designs that use a black background but we're open to new ideas.

I have attached a few files:

-A simple wire frame example to show how this card could look with the different elements mentioned above, feel free to use a layout similar to this or come up with something totally different (biz-card.pdf)
-Front and back of a loyalty card the we've used in the past (this card was printed on plastic)
-Front and back of a key fob design that we've previously used (this card was printed on plastic)
-A logo file with the 12 small icons and the main logo image

If you need further images or information please ask.

```html
<!DOCTYPE html>
<html lang="en">
<head>
<meta charset="utf-8">
<title>HNR – Business Card</title>
<link rel="stylesheet" href="https://fonts.googleapis.com/css2?family=Open+Sans:wght@400;600;700;800&display=swap">
<style>
  :root {
    --bg: #ecedef;
    --black: #111214;
    --charcoal: #2c2e31;
    --grey-light: #d9dbde;
    --grey-dark: #a6aaaf;
    --blue-bright: #2167d3;
    --blue-deep: #2b2a96;
    --accent-blue: #2a8fe0;
    --red: #e3242b;
    --white: #ffffff;
    --text-dark: #1a1a1a;
    --text-muted: #4a4d52;
  }
  * { box-sizing: border-box; margin: 0; padding: 0; }
  html, body { width: 1200px; height: 873px; overflow: hidden; }
  body {
    background: var(--bg);
    font-family: "Open Sans", Arial, sans-serif;
    position: relative;
  }
  .card {
    position: absolute;
    top: 262px;
    width: 540px;
    height: 350px;
    border-radius: 6px;
    overflow: hidden;
    box-shadow: 0 10px 30px rgba(0,0,0,0.18);
  }
  .card--back { left: 40px; }
  .card--front { left: 620px; }
  .card__shapes { position: absolute; inset: 0; }

  /* Back: trades + feedback */
  .trade-icons {
    position: absolute;
    left: 18px; top: 30px;
    display: grid;
    grid-template-columns: repeat(3, 34px);
    gap: 22px 10px;
  }
  .trade-icon {
    width: 34px; height: 34px;
    border-radius: 7px;
    box-shadow: 0 2px 3px rgba(0,0,0,0.3);
  }
  .tagline {
    position: absolute;
    right: 22px; top: 26px;
    color: var(--white);
    font-weight: 700;
    font-size: 25px;
    line-height: 1.2;
    white-space: nowrap;
  }
  .tradesman-label {
    position: absolute;
    left: 205px; top: 100px;
    color: var(--white);
    font-size: 11px;
    line-height: 14px;
  }
  .tradesman-box {
    position: absolute;
    left: 205px; top: 118px;
    width: 310px; height: 62px;
    background: var(--white);
  }
  .feedback-title {
    position: absolute;
    left: 205px; top: 200px;
    color: var(--white);
    font-weight: 700;
    font-size: 18px;
    line-height: 24px;
    white-space: nowrap;
  }
  .feedback-text {
    position: absolute;
    left: 205px; top: 232px;
    color: var(--white);
    font-size: 14px;
    line-height: 20px;
    white-space: nowrap;
  }

  /* Front: brand + offer */
  .brand {
    position: absolute;
    left: 40px; top: 38px;
    color: var(--white);
  }
  .brand__name {
    font-weight: 800;
    font-size: 64px;
    line-height: 1;
    letter-spacing: 1px;
  }
  .brand__strap {
    margin-top: 8px;
    font-weight: 700;
    font-size: 20px;
  }
  .contact {
    position: absolute;
    left: 40px; top: 215px;
    color: var(--white);
  }
  .contact__phone {
    display: flex;
    align-items: center;
    gap: 10px;
    font-weight: 600;
    font-size: 27px;
  }
  .contact__icon {
    width: 30px; height: 30px;
    border-radius: 5px;
    background: var(--accent-blue);
    display: flex; align-items: center; justify-content: center;
  }
  .contact__web {
    margin-top: 6px;
    margin-left: 40px;
    font-size: 18px;
  }
  .offer {
    position: absolute;
    right: 18px; top: 86px;
    width: 170px;
    text-align: center;
  }
  .offer__amount {
    color: var(--red);
    font-weight: 800;
    font-size: 66px;
    line-height: 1;
  }
  .offer__word {
    color: var(--text-dark);
    font-weight: 800;
    font-size: 34px;
    line-height: 1.05;
  }
  .offer__sub {
    color: var(--text-dark);
    font-weight: 600;
    font-size: 20px;
  }
  .offer__note {
    margin-top: 16px;
    color: var(--text-muted);
    font-size: 11px;
    line-height: 14px;
  }
</style>
</head>
<body>

<section class="card card--back" aria-label="Card back: trades and feedback">
  <svg class="card__shapes" width="540" height="350" viewBox="0 0 540 350" aria-hidden="true">
    <defs>
      <linearGradient id="back-blue" x1="0" y1="0" x2="1" y2="1">
        <stop offset="0" stop-color="var(--blue-bright)"/>
        <stop offset="1" stop-color="var(--blue-deep)"/>
      </linearGradient>
      <linearGradient id="back-grey" x1="0" y1="0" x2="1" y2="0">
        <stop offset="0" stop-color="var(--grey-light)"/>
        <stop offset="1" stop-color="var(--grey-dark)"/>
      </linearGradient>
    </defs>
    <rect width="540" height="350" fill="url(#back-blue)"/>
    <path d="M150 0 H540 V82 H176 Q168 40 150 0 Z" fill="var(--black)"/>
    <path d="M0 0 H150 Q195 175 150 350 H0 Z" fill="url(#back-grey)"/>
  </svg>

  <div class="trade-icons" role="img" aria-label="Twelve trade icons: plumbing, electrics, carpentry, decorating, heating and more">
    <span class="trade-icon" style="background:#2a8fe0"></span>
    <span class="trade-icon" style="background:#6bb83a"></span>
    <span class="trade-icon" style="background:#2a8fe0"></span>
    <span class="trade-icon" style="background:#e3242b"></span>
    <span class="trade-icon" style="background:#c6d12e"></span>
    <span class="trade-icon" style="background:#8a8f96"></span>
    <span class="trade-icon" style="background:#2a8fe0"></span>
    <span class="trade-icon" style="background:#f0b323"></span>
    <span class="trade-icon" style="background:#2a8fe0"></span>
    <span class="trade-icon" style="background:#b9774a"></span>
    <span class="trade-icon" style="background:#8a8f96"></span>
    <span class="trade-icon" style="background:#c02c8f"></span>
  </div>

  <h2 class="tagline">Your local all-trade experts</h2>
  <p class="tradesman-label">Your HNR tradesman:</p>
  <div class="tradesman-box"></div>
  <h3 class="feedback-title">What do you think of our service?</h3>
  <p class="feedback-text">Please leave feedback online<br>www.hnr-services.example/feedback</p>
</section>

<section class="card card--front" aria-label="Card front: brand and discount offer">
  <svg class="card__shapes" width="540" height="350" viewBox="0 0 540 350" aria-hidden="true">
    <defs>
      <radialGradient id="front-black" cx="0.35" cy="0.4" r="0.7">
        <stop offset="0" stop-color="var(--charcoal)"/>
        <stop offset="1" stop-color="var(--black)"/>
      </radialGradient>
      <linearGradient id="front-grey" x1="0" y1="0" x2="1" y2="0">
        <stop offset="0" stop-color="var(--grey-dark)"/>
        <stop offset="1" stop-color="var(--grey-light)"/>
      </linearGradient>
    </defs>
    <rect width="540" height="350" fill="url(#front-black)"/>
    <path d="M360 0 Q315 175 360 350 H540 V0 Z" fill="url(#front-grey)"/>
  </svg>

  <div class="brand">
    <div class="brand__name">HNR</div>
    <div class="brand__strap">Expert Property Care</div>
  </div>

  <div class="contact">
    <div class="contact__phone">
      <span class="contact__icon">
        <svg width="18" height="18" viewBox="0 0 24 24" aria-hidden="true">
          <path fill="#fff" d="M6.6 10.8a15.1 15.1 0 0 0 6.6 6.6l2.2-2.2a1 1 0 0 1 1-.25 11.4 11.4 0 0 0 3.6.6 1 1 0 0 1 1 1V20a1 1 0 0 1-1 1A17 17 0 0 1 3 4a1 1 0 0 1 1-1h3.5a1 1 0 0 1 1 1c0 1.250.2 2.450.57 3.570a1 1 0 0 1-.25 1z"/>
        </svg>
      </span>
      0800 555 0142
    </div>
    <div class="contact__web">hnr-services.example</div>
  </div>

  <div class="offer">
    <div class="offer__amount">10%</div>
    <div class="offer__word">discount</div>
    <div class="offer__sub">with this card</div>
    <p class="offer__note">Check our website<br>for full offer details</p>
  </div>
</section>

</body>
</html>
```